skincare creams for tired moms

I need a package and a logo design for a skincare company based in California called Lumen Petal. I make day and night cream, under eye cream, and body lotion. The first product I plan to launch is an under eye cream. It does not have to be in these colors but I do teals, greens, black, and cobalt blue.

The package is going to either be in a box or a bag. Either way I go it will be like a gift box or bag. The design should make the person feel like they are getting something special and luxurious just for them.

I have small kids and it is really difficult to find a chunk of time to myself to update or review.

Target Market(s)

mainly first time moms. I am making an under eye cream that does not use retinol but is still powerful enough to get rid of bags and dark circles.

Industry/Entity Type

Cosmetics

Logo Text

The package and logo should incorporate the name Lumen Petal.

Font styles to use
Decorative
Script

Colors

Designer to choose colors to be used in the design.

Requirements
Nice to have
• maybe focus more on Petal instead of Lumen. Also incorporate plants or flowers
Should not have
• not a huge fan of pink

```html
<!DOCTYPE html>
<html lang="en">
<head>
<meta charset="utf-8">
<title>Lumen Petal – under eye cream label</title>
<link href="https://fonts.googleapis.com/css2?family=Barlow+Condensed:ital,wght@0,300;0,400;1,600&display=swap" rel="stylesheet">
<style>
  :root {
    --backdrop: #3a3a3c;
    --label: #ffffff;
    --teal: #128581;
    --teal-ink: #1a8a85;
    --on-teal: #ffffff;
  }
  * { margin: 0; padding: 0; box-sizing: border-box; }
  html, body { width: 1200px; height: 845px; overflow: hidden; }
  body {
    background: var(--backdrop);
    font-family: "Barlow Condensed", "Arial Narrow", sans-serif;
    position: relative;
  }
  .label {
    position: absolute;
    left: 363px;
    top: 65px;
    width: 474px;
    height: 714px;
    background: var(--label);
  }
  .brand-mark {
    position: absolute;
    top: 78px;
    left: 0;
    width: 100%;
    display: flex;
    justify-content: center;
    align-items: center;
    gap: 10px;
    color: var(--teal);
  }
  .brand-mark__dot {
    width: 34px;
    height: 34px;
    border-radius: 50%;
    background: var(--teal);
  }
  .brand-mark__name {
    font-weight: 400;
    font-size: 30px;
    letter-spacing: 0.5px;
  }
  .title-band {
    position: absolute;
    top: 234px;
    left: 0;
    width: 100%;
    height: 128px;
    background: var(--teal);
    color: var(--on-teal);
    text-align: center;
  }
  .product-name {
    font-weight: 300;
    font-size: 52px;
    line-height: 1;
    margin-top: 24px;
    letter-spacing: 0.5px;
  }
  .product-type {
    font-weight: 600;
    font-style: italic;
    font-size: 30px;
    line-height: 1;
    margin-top: 8px;
    letter-spacing: 0.3px;
  }
  .botanical {
    position: absolute;
    top: 375px;
    left: 195px;
    width: 84px;
    height: 120px;
    background: linear-gradient(160deg, #d6ecea, #b5dcd9);
    border-radius: 6px;
  }
  .volume {
    position: absolute;
    top: 524px;
    width: 100%;
    text-align: center;
    color: var(--teal-ink);
    font-weight: 400;
    font-size: 18px;
  }
  .actives {
    position: absolute;
    top: 572px;
    width: 100%;
    text-align: center;
    color: var(--teal-ink);
    font-weight: 400;
    font-size: 30px;
    line-height: 34px;
  }
</style>
</head>
<body>
  <main class="label">
    <div class="brand-mark">
      <span class="brand-mark__dot"></span>
      <span class="brand-mark__name">Lumen Petal</span>
    </div>

    <header class="title-band">
      <h1 class="product-name">Lumen Petal</h1>
      <p class="product-type">under eye cream</p>
    </header>

    <div class="botanical" role="img" aria-label="Line drawing of a leafy sprig with small berries"></div>

    <p class="volume">0.5fl.oz (15ml)</p>

    <p class="actives">Hyaluronic acid+<br>halovex ocuvera</p>
  </main>
</body>
</html>
```